Stationery for Heating Plumbing & Electrical Contractor
Veltrana
Stationery for Heating Plumbing & Electrical Contractor - Construction
Creative Brief
Professional
Neil Farrow
Director
428b Pellham Rd , Oakvane, Warrington , Cheshire QX7 3PZ
Mornwick@fenmail.com
www.veltrana.uk.com

```html
<!DOCTYPE html>
<html lang="en">
<head>
<meta charset="utf-8">
<title>Veltrana – Business Card</title>
<link href="https://fonts.googleapis.com/css2?family=Open+Sans:ital,wght@0,400;0,600;0,700;1,400&display=swap" rel="stylesheet">
<style>
  :root {
    --canvas: #d6d6d6;
    --card-white: #ffffff;
    --charcoal: #3f3f41;
    --charcoal-light: #5a5a5c;
    --silver: #c4c4c6;
    --orange: #f5a623;
    --orange-deep: #e8891a;
    --navy: #1d2a48;
    --text-grey: #555555;
  }
  * { margin: 0; padding: 0; box-sizing: border-box; }
  html, body { width: 1200px; height: 878px; overflow: hidden; }
  body {
    background: var(--canvas);
    font-family: "Open Sans", Arial, sans-serif;
    position: relative;
  }
  .card {
    position: absolute;
    top: 284px;
    width: 540px;
    height: 310px;
    overflow: hidden;
    box-shadow: 0 6px 18px rgba(0,0,0,0.18);
  }
  .card--front { left: 40px; background: var(--card-white); }
  .card--back {
    left: 620px;
    background: linear-gradient(135deg, var(--charcoal-light), var(--charcoal));
  }
  .card-shapes { position: absolute; inset: 0; }

  .brand {
    position: absolute;
    left: 26px;
    top: 30px;
    display: flex;
    align-items: center;
    gap: 10px;
  }
  .brand-dot {
    width: 34px; height: 34px;
    border-radius: 50%;
    background: var(--orange);
  }
  .brand-name {
    font-size: 36px;
    font-weight: 400;
    color: var(--charcoal);
    letter-spacing: 0.5px;
  }

  .contact {
    position: absolute;
    left: 300px;
    top: 96px;
    color: var(--text-grey);
  }
  .contact-name {
    font-size: 17px;
    font-weight: 700;
    color: var(--navy);
  }
  .contact-role {
    font-size: 11px;
    font-style: italic;
    color: var(--orange-deep);
    margin-bottom: 8px;
  }
  .contact-address { font-size: 10.5px; line-height: 1.35; margin-bottom: 8px; }
  .contact-list { list-style: none; font-size: 10.5px; line-height: 1.6; }
  .contact-list li { display: flex; align-items: center; gap: 7px; }
  .contact-icon { width: 9px; height: 9px; flex: none; }
  .contact-icon .icon-fill { fill: var(--orange-deep); }

  .website {
    position: absolute;
    left: 200px;
    top: 282px;
    font-size: 11px;
    color: #ffffff;
    letter-spacing: 0.5px;
  }

  .back-name {
    position: absolute;
    right: 34px;
    bottom: 34px;
    font-size: 64px;
    font-weight: 400;
    color: var(--silver);
    letter-spacing: 1px;
  }
</style>
</head>
<body>

  <section class="card card--front" aria-label="Business card front">
    <svg class="card-shapes" viewBox="0 0 540 310" aria-hidden="true">
      <defs>
        <linearGradient id="orangeBand" x1="0" y1="0" x2="1" y2="1">
          <stop offset="0" stop-color="#f7b733"/>
          <stop offset="1" stop-color="#e8891a"/>
        </linearGradient>
      </defs>
      <polygon points="0,150 12,150 12,256 160,272 0,272" fill="url(#orangeBand)"/>
      <rect x="0" y="272" width="540" height="38" fill="var(--charcoal)"/>
      <rect x="160" y="268" width="380" height="4" fill="var(--orange)"/>
    </svg>

    <div class="brand">
      <span class="brand-dot"></span>
      <span class="brand-name">veltrana</span>
    </div>

    <div class="contact">
      <p class="contact-name">Neil Farrow</p>
      <p class="contact-role">Managing Director</p>
      <p class="contact-address">428b Pellham Rd<br>Oakvane QX7 3PZ</p>
      <ul class="contact-list">
        <li><svg class="contact-icon" viewBox="0 0 10 10"><path class="icon-fill" d="M2 0h2l1 3-1.5 1a6 6 0 0 0 2.5 2.5L7 5l3 1v2a2 2 0 0 1-2 2A8 8 0 0 1 0 2a2 2 0 0 1 2-2z"/></svg>0192 548 3216</li>
        <li><svg class="contact-icon" viewBox="0 0 10 10"><path class="icon-fill" d="M2 0h2l1 3-1.5 1a6 6 0 0 0 2.5 2.5L7 5l3 1v2a2 2 0 0 1-2 2A8 8 0 0 1 0 2a2 2 0 0 1 2-2z"/></svg>0192 548 3217</li>
        <li><svg class="contact-icon" viewBox="0 0 10 10"><rect class="icon-fill" x="0" y="3" width="10" height="6" rx="1"/><rect class="icon-fill" x="2" y="0" width="6" height="2.5"/></svg>0192 548 3290</li>
        <li><svg class="contact-icon" viewBox="0 0 10 10"><rect class="icon-fill" x="2.5" y="0" width="5" height="10" rx="1"/></svg>0770 091 4352</li>
        <li><svg class="contact-icon" viewBox="0 0 10 10"><rect class="icon-fill" x="0" y="2" width="10" height="6.5" rx="0.8"/><path d="M0.5 2.5L5 5.8 9.5 2.5" fill="none" stroke="#ffffff" stroke-width="0.9"/></svg>mornwick@fenmail.com</li>
      </ul>
    </div>

    <p class="website">www.veltrana.uk.com</p>
  </section>

  <section class="card card--back" aria-label="Business card back">
    <p class="back-name">veltrana</p>
  </section>

</body>
</html>
```